New Infographic Design Project

Hi, I have another project to work on if you are interested. It is a horizontal style infographic with 6 steps. It should display the step Number (1-6), Title, and an Icon.

Step 1 - Strong Phone Interview
Step 2 - Pre-Employment
Step 3 - Prep & Do In-Person Interview
Step 4 - Second Interview
Step 5 - Reference Checks
Step 6 - Job Offer

More flexible on colors with this one, but keep it professional.

```html
<!DOCTYPE html>
<html lang="en">
<head>
<meta charset="utf-8">
<title>Hiring Process – 6 Steps</title>
<link rel="stylesheet" href="https://fonts.googleapis.com/css2?family=Montserrat:wght@700&family=Open+Sans:wght@500&display=swap">
<style>
  :root {
    --bg: #363636;
    --yellow: #fbbf24;
    --blue: #1aa9e1;
    --green: #7cc242;
    --purple: #a585c2;
    --coral: #f26a57;
    --teal: #31b6b3;
    --label: #dcdcdc;
    --body: #ffffff;
    --icon: #2b2b2b;
  }
  * { margin: 0; padding: 0; box-sizing: border-box; }
  html, body { width: 1200px; height: 400px; overflow: hidden; background: var(--bg); }
  .infographic { position: relative; width: 1200px; height: 400px; background: var(--bg); }
  .chain { position: absolute; left: 0; top: 0; }
  .step {
    position: absolute; top: 0; width: 180px; margin-left: -90px;
    text-align: center; height: 400px;
  }
  .step-title {
    position: absolute; top: 40px; left: 0; right: 0; height: 36px;
    display: flex; align-items: center; justify-content: center;
    font-family: "Montserrat", sans-serif; font-weight: 700; font-size: 13.5px;
    line-height: 17px; text-transform: uppercase;
  }
  .step-number {
    position: absolute; top: 273px; left: 0; right: 0;
    font-family: "Montserrat", sans-serif; font-weight: 700; font-size: 15.5px;
    color: var(--label); letter-spacing: 0.3px;
  }
  .step-text {
    position: absolute; top: 296px; left: 0; right: 0;
    font-family: "Open Sans", sans-serif; font-weight: 500; font-size: 11.6px;
    line-height: 14.7px; color: var(--body);
  }
  .s1 { left: 129px; } .s1 .step-title { color: var(--yellow); }
  .s2 { left: 318px; } .s2 .step-title { color: var(--blue); }
  .s3 { left: 506px; } .s3 .step-title { color: var(--green); }
  .s4 { left: 694px; } .s4 .step-title { color: var(--purple); }
  .s5 { left: 882px; } .s5 .step-title { color: var(--coral); }
  .s6 { left: 1070px; } .s6 .step-title { color: var(--teal); }
</style>
</head>
<body>
<main class="infographic">
  <svg class="chain" width="1200" height="400" viewBox="0 0 1200 400">
    <defs>
      <radialGradient id="face" cx="50%" cy="40%" r="60%">
        <stop offset="0%" stop-color="#ffffff"/>
        <stop offset="100%" stop-color="#e4e4e4"/>
      </radialGradient>
      <filter id="lift" x="-20%" y="-20%" width="140%" height="140%">
        <feDropShadow dx="2" dy="3" stdDeviation="3" flood-color="#000" flood-opacity="0.3"/>
      </filter>
    </defs>

    <!-- connectors -->
    <path d="M180,140 Q224,162 268,140 L268,204 Q224,182 180,204 Z" fill="var(--yellow)"/>
    <path d="M369,140 Q412,162 456,140 L456,204 Q412,182 369,204 Z" fill="var(--blue)"/>
    <path d="M557,140 Q600,162 644,140 L644,204 Q600,182 557,204 Z" fill="var(--green)"/>
    <path d="M745,140 Q788,162 832,140 L832,204 Q788,182 745,204 Z" fill="var(--purple)"/>
    <path d="M933,140 Q976,162 1020,140 L1020,204 Q976,182 933,204 Z" fill="var(--coral)"/>

    <!-- rings -->
    <g class="rings">
      <circle cx="129" cy="172" r="72" fill="var(--yellow)"/>
      <circle cx="318" cy="172" r="72" fill="var(--blue)"/>
      <circle cx="506" cy="172" r="72" fill="var(--green)"/>
      <circle cx="694" cy="172" r="72" fill="var(--purple)"/>
      <circle cx="882" cy="172" r="72" fill="var(--coral)"/>
      <circle cx="1070" cy="172" r="72" fill="var(--teal)"/>
    </g>

    <!-- faces -->
    <g class="faces" fill="url(#face)" filter="url(#lift)">
      <circle cx="129" cy="172" r="61"/>
      <circle cx="318" cy="172" r="61"/>
      <circle cx="506" cy="172" r="61"/>
      <circle cx="694" cy="172" r="61"/>
      <circle cx="882" cy="172" r="61"/>
      <circle cx="1070" cy="172" r="61"/>
    </g>

    <!-- icon: phone -->
    <g class="icon-phone" fill="var(--icon)">
      <path d="M95,154 c4,-4 10,-3 12,1 l6,10 c2,4 0,7 -3,9 l-3,2 c2,7 9,16 16,19 l3,-3 c3,-3 6,-3 9,-1 l9,7 c3,3 3,8 -1,11 l-5,4 c-8,6 -25,-2 -38,-17 c-11,-14 -15,-28 -9,-36 Z"/>
      <circle cx="139" cy="158" r="14" fill="none" stroke="var(--icon)" stroke-width="4"/>
      <line x1="149" y1="168" x2="160" y2="179" stroke="var(--icon)" stroke-width="5" stroke-linecap="round"/>
    </g>

    <!-- icon: tick -->
    <path class="icon-tick" d="M298,172 l14,14 l26,-28" fill="none" stroke="var(--icon)" stroke-width="6" stroke-linecap="round" stroke-linejoin="round"/>

    <!-- scene placeholders -->
    <circle cx="506" cy="172" r="44" fill="#d9d9d9" role="img" aria-label="Icon: candidate meeting interview panel at a table"/>
    <circle cx="694" cy="172" r="44" fill="#d9d9d9" role="img" aria-label="Icon: two people seated across a table for a second interview"/>
    <circle cx="882" cy="172" r="44" fill="#d9d9d9" role="img" aria-label="Icon: magnifying glass over a candidate profile"/>

    <!-- icon: briefcase -->
    <g class="icon-briefcase" fill="none" stroke="var(--icon)" stroke-width="4" stroke-linejoin="round">
      <rect x="1046" y="158" width="48" height="34" rx="4"/>
      <path d="M1060,158 v-7 h20 v7"/>
      <line x1="1046" y1="172" x2="1094" y2="172"/>
    </g>
  </svg>

  <section class="step s1">
    <h2 class="step-title">Strong Phone<br>Interview</h2>
    <p class="step-number">STEP 1</p>
    <p class="step-text">Lorem ipsum dolor sit amet, consectetuer adipiscing elit, sed diam nonummy nibh euismod</p>
  </section>
  <section class="step s2">
    <h2 class="step-title">Pre-Employment</h2>
    <p class="step-number">STEP 2</p>
    <p class="step-text">Lorem ipsum dolor sit amet, consectetuer adipiscing elit, sed diam nonummy nibh euismod</p>
  </section>
  <section class="step s3">
    <h2 class="step-title">Prep &amp; Do In-Person<br>Interview</h2>
    <p class="step-number">STEP 3</p>
    <p class="step-text">Lorem ipsum dolor sit amet, consectetuer adipiscing elit, sed diam nonummy nibh euismod</p>
  </section>
  <section class="step s4">
    <h2 class="step-title">Second<br>Interview</h2>
    <p class="step-number">STEP 4</p>
    <p class="step-text">Lorem ipsum dolor sit amet, consectetuer adipiscing elit, sed diam nonummy nibh euismod</p>
  </section>
  <section class="step s5">
    <h2 class="step-title">Reference<br>Checks</h2>
    <p class="step-number">STEP 5</p>
    <p class="step-text">Lorem ipsum dolor sit amet, consectetuer adipiscing elit, sed diam nonummy nibh euismod</p>
  </section>
  <section class="step s6">
    <h2 class="step-title">Job Offer</h2>
    <p class="step-number">STEP 6</p>
    <p class="step-text">Lorem ipsum dolor sit amet, consectetuer adipiscing elit, sed diam nonummy nibh euismod</p>
  </section>
</main>
</body>
</html>
```